Flyer / Mailer for Business Debt Relief Business - Tillbrook Partners 6" x 11"

We need a 6" x 11" double sided flyer. This will be sent out to potential customers with high interest business loans. We would like the design to coordinate with the colors of our logo. I have included a mock up that we sketched out. I have also included a file of a mailer we received that we would like to use as a template (not colors or fonts, just set up). I have also included an .ai file of our logo.

```html
<!DOCTYPE html>
<html lang="en">
<head>
<meta charset="utf-8">
<title>Tillbrook Partners – Business Debt Relief Mailer</title>
<link href="https://fonts.googleapis.com/css2?family=Lexend:wght@300;400;600&family=Roboto+Condensed:wght@400&family=Playfair+Display:ital,wght@1,700&display=swap" rel="stylesheet">
<style>
  :root {
    --blue: #0a6ab3;
    --blue-dark: #0a5a9c;
    --blue-pale: #dff3fb;
    --green: #52ad32;
    --green-dark: #3f9a25;
    --ink: #111;
    --grey-text: #555;
    --backdrop: #808285;
    --white: #fff;
  }
  * { box-sizing: border-box; margin: 0; padding: 0; }
  html, body { width: 1200px; height: 1200px; overflow: hidden; }
  body { background: var(--backdrop); font-family: "Lexend", sans-serif; position: relative; }

  .card { position: absolute; left: 160px; width: 880px; height: 480px; overflow: hidden; }
  .card--front { top: 60px; background: radial-gradient(circle at 60% 45%, #f4fcff 0%, var(--blue-pale) 70%, #c9ebf7 100%); }
  .card--back { top: 640px; background: var(--white); }

  .front-shapes { position: absolute; inset: 0; }
  .photo { position: absolute; border-radius: 50%; }
  .photo--savings { left: 58px; top: 18px; width: 138px; height: 138px; background: radial-gradient(circle, #f3c7d3 0%, #c7ccb5 60%, #8f9a80 100%); border: 3px solid var(--green); }
  .photo--cash { left: 91px; top: 172px; width: 138px; height: 138px; background: radial-gradient(circle, #d8dccd 0%, #9aa38e 70%, #6f7865 100%); }
  .photo--seedling { left: 50px; top: 322px; width: 138px; height: 138px; background: radial-gradient(circle at 50% 60%, #7aa64a 0%, #9bbf6f 45%, #c8d8b4 100%); border: 3px solid var(--blue); }
  .photo--person { position: absolute; left: 585px; top: 83px; width: 295px; height: 397px; background: linear-gradient(180deg, rgba(220,200,180,0) 0%, #c9ad95 30%, #24324f 55%, #1c2a45 100%); border-radius: 140px 140px 0 0; }

  .headline { position: absolute; left: 211px; top: 20px; font-size: 25px; font-weight: 300; color: var(--ink); white-space: nowrap; }
  .headline strong { font-weight: 600; color: var(--blue); }
  .banner-text { position: absolute; left: 237px; top: 64px; font-family: "Playfair Display", serif; font-style: italic; font-weight: 700; font-size: 17px; line-height: 21px; color: var(--white); }
  .question { position: absolute; left: 245px; top: 124px; font-size: 19px; font-weight: 600; color: var(--blue); }
  .cta-big { position: absolute; left: 245px; top: 148px; font-size: 27px; font-weight: 600; color: var(--green); letter-spacing: -0.5px; }
  .benefits { position: absolute; left: 245px; top: 190px; list-style: none; font-family: "Roboto Condensed", sans-serif; font-size: 16px; line-height: 21px; color: var(--ink); }
  .benefits li::before { content: "•"; color: var(--blue); margin-right: 5px; }

  .contact { position: absolute; left: 247px; top: 393px; width: 320px; text-align: center; color: var(--white); }
  .contact__web { font-size: 15px; font-weight: 300; white-space: nowrap; }
  .contact__web b { font-weight: 600; }
  .contact__note { font-size: 10px; font-weight: 300; margin-top: 1px; }
  .contact__phone { font-size: 23px; font-weight: 600; letter-spacing: 0.5px; line-height: 28px; }
  .contact__mail { font-size: 14px; font-weight: 600; }

  .brand { position: absolute; display: flex; align-items: center; gap: 6px; font-size: 13px; font-weight: 400; color: #333; white-space: nowrap; }
  .brand__mark { width: 12px; height: 12px; background: var(--green); }
  .brand--front { right: 10px; top: 74px; }
  .brand--back { left: 140px; top: 78px; font-size: 16px; }
  .brand-sub { position: absolute; font-size: 7px; color: #333; letter-spacing: 0.3px; }
  .brand-sub--front { right: 50px; top: 92px; }
  .brand-sub--back { left: 188px; top: 100px; }

  .address { position: absolute; left: 75px; top: 116px; width: 285px; border-top: 1px solid #ccc; border-bottom: 1px solid #ccc; padding: 4px 0 5px; font-size: 10.5px; font-weight: 300; color: var(--grey-text); text-align: center; }
  .back-title { position: absolute; left: 40px; top: 174px; width: 360px; text-align: center; font-family: "Playfair Display", serif; font-style: italic; font-weight: 700; font-size: 27px; line-height: 37px; color: var(--blue); }
  .back-copy { position: absolute; left: 60px; top: 266px; width: 320px; text-align: center; font-size: 18px; font-weight: 300; line-height: 27px; color: var(--ink); }
  .call-box { position: absolute; left: 84px; top: 405px; width: 273px; height: 57px; background: var(--blue); border-radius: 2px; color: var(--white); text-align: center; padding-top: 6px; }
  .call-box__note { font-size: 11px; font-weight: 300; }
  .call-box__phone { font-size: 26px; font-weight: 600; line-height: 30px; }
  .call-box-fold { position: absolute; left: 64px; top: 422px; }
  .divider { position: absolute; left: 439px; top: 78px; width: 2px; height: 324px; background: #7aaed6; }
  .stamp { position: absolute; left: 766px; top: 42px; width: 64px; height: 76px; border: 1px solid #999; }
  .base-stripe { position: absolute; left: 0; bottom: 0; width: 100%; height: 6px; background: var(--green); }
</style>
</head>
<body>

<section class="card card--front" aria-label="Mailer front">
  <svg class="front-shapes" width="880" height="480" viewBox="0 0 880 480" aria-hidden="true">
    <path d="M0 0 H80 Q30 150 75 300 Q110 420 80 480 H0 Z" fill="var(--blue)"/>
    <circle cx="127" cy="87" r="81" fill="#bfe0f1" opacity="0.9"/>
    <circle cx="160" cy="241" r="81" fill="#d6ecf6"/>
    <circle cx="119" cy="391" r="81" fill="#bfe0f1" opacity="0.9"/>
    <path d="M205 61 H686 L662 113 H205 Z" fill="var(--green)"/>
    <path d="M692 61 H700 L676 113 H668 Z" fill="var(--blue)"/>
    <path d="M706 61 H713 L689 113 H682 Z" fill="var(--blue)"/>
    <path d="M95 389 H880 V480 H60 Q90 440 95 389 Z" fill="var(--green)"/>
  </svg>

  <div class="photo photo--savings" role="img" aria-label="Photo of a pink piggy bank on banknotes"></div>
  <div class="photo photo--cash" role="img" aria-label="Photo of a stack of dollar bills"></div>
  <div class="photo photo--seedling" role="img" aria-label="Photo of hands holding a young seedling in soil"></div>
  <div class="photo--person" role="img" aria-label="Photo of a smiling businessman in a navy blazer, hand on chin"></div>

  <h1 class="headline">Helping Business <strong>Focus On What Metters!</strong></h1>
  <p class="banner-text">We understand that merchant cash advance loans can<br>be a burden on your business</p>
  <p class="question">Over whelmed by daily / weekly payments?</p>
  <p class="cta-big">WE CAN HELP!</p>
  <ul class="benefits">
    <li>This is not loan, WE ARE NOT LENDERS!</li>
    <li>Improve your business’s cash flow immediately</li>
    <li>Move payments to one monthly amount</li>
    <li>Reduce the amount you are pay’s out monthly</li>
    <li>Strategic alternatives to his interest loans</li>
    <li>Fast, Confidential business debt relief</li>
    <li>No-oblisetion consultation</li>
    <li>Absolutely no credit polls</li>
    <li>No collateral, no financials</li>
  </ul>

  <div class="contact">
    <p class="contact__web">Visit our website <b>www.tillbrookpartners.com</b></p>
    <p class="contact__note">Call now for free consultation with our Experts</p>
    <p class="contact__phone">555-274-8810</p>
    <p class="contact__mail">E-mail: info@tillbrookpartners.com</p>
  </div>

  <div class="brand brand--front"><span class="brand__mark"></span>TILLBROOK PARTNERS</div>
  <span class="brand-sub brand-sub--front">CONSULTING</span>
</section>

<section class="card card--back" aria-label="Mailer back">
  <div class="brand brand--back"><span class="brand__mark"></span>TILLBROOK PARTNERS</div>
  <span class="brand-sub brand-sub--back">CONSULTING</span>
  <p class="address">418 Harlow Ave Brenton, Marlow County 70412 - USA</p>

  <h2 class="back-title">Stvetesic Debit relief for<br>Businesses of All Sizes</h2>
  <p class="back-copy">Stop takins out loans to<br>pay off other loans.<br>Take back your business's<br>cash flow, and focus on<br>that matters.</p>

  <svg class="call-box-fold" width="22" height="40" viewBox="0 0 22 40" aria-hidden="true"><path d="M0 0 H20 V40 Z" fill="#c8c8c8"/></svg>
  <div class="call-box">
    <p class="call-box__note">Call now for free consultation with our Experts</p>
    <p class="call-box__phone">555-274-8810</p>
  </div>

  <div class="divider"></div>
  <div class="stamp"></div>
  <div class="base-stripe"></div>
</section>

</body>
</html>
```